Flyer for the Radiant Harvest Worship Day

I am looking to create a flyer for a one day prayer retreat our church is organizing.
This flyer will be posted on social media, websites and will also be printed so it can be mailed to people.
I am looking for something professional, with good use of our logo and band colors (logo colors).
I am counting on the designer's skill, creativity, art and knowledge of media communication to produce a flyer that will effectively and quickly convey the message we are trying to spread.
CONTENT OF THE FLYER:
Event title: Radiant Harvest Worship Day
Date: Tuesday July 2nd, 2019
Time: 11:00AM - 7:00PM
Wexmoor Hotel, 4817 Ballard Avenue, Portland, Maine 04102 (Room: Larkspur)
Event Key words to highlight what the event is about: Prayer, Sharing the Word, Panel discussion, prophecy, Impartation.
Key phrases:
A one day prayer retreat.
Jesus Chris is Lord
Contact info:
www.velodu.org
Phone: 207 555 0148
Email: contact@brightmeadow.org

```html
<!DOCTYPE html>
<html lang="en">
<head>
<meta charset="utf-8">
<title>Radiant Harvest Worship Day</title>
<link href="https://fonts.googleapis.com/css2?family=Arimo:wght@400;700&display=swap" rel="stylesheet">
<style>
  :root {
    --navy: #0f3a63;
    --orange: #f39a21;
    --white: #ffffff;
    --rule: #6f8aa6;
    --frame: #9a9a9a;
    --sky-top: #6e5a66;
    --sky-mid: #c4854f;
    --sky-low: #4a3226;
  }
  * { box-sizing: border-box; margin: 0; padding: 0; }
  html, body { width: 875px; height: 1200px; overflow: hidden; background: var(--white); }
  body { font-family: "Arimo", Arial, sans-serif; color: var(--white); position: relative; }
  .sheet-frame { position: absolute; inset: 0; border: 1px solid var(--frame); }
  .flyer { position: absolute; left: 44px; top: 43px; width: 768px; height: 1085px; background: var(--navy); overflow: hidden; }
  .hero-photo {
    position: absolute; left: 0; top: 32px; width: 768px; height: 530px;
    background: linear-gradient(180deg, var(--sky-top) 0%, var(--sky-mid) 60%, var(--sky-low) 100%);
  }
  .brand-box { position: absolute; left: 63px; top: 32px; width: 201px; height: 168px; background: var(--navy); display: flex; align-items: center; justify-content: center; }
  .brand-name { font-weight: 700; font-size: 40px; letter-spacing: 1px; color: var(--white); }
  .event-title { position: absolute; left: 62px; top: 394px; text-transform: uppercase; font-weight: 700; line-height: 1; }
  .event-title .line-one { display: block; font-size: 51px; }
  .event-title .line-two { display: block; font-size: 73px; margin-top: 8px; }
  .tagline-band { position: absolute; left: 0; top: 576px; width: 768px; height: 94px; background: var(--orange); text-align: center; text-transform: uppercase; }
  .tagline-band .retreat { font-size: 33px; margin-top: 6px; line-height: 1.1; }
  .tagline-band .lordship { font-size: 45px; font-weight: 700; line-height: 1.1; }
  .keywords { position: absolute; left: 0; top: 701px; width: 768px; text-align: center; font-weight: 700; font-size: 29px; line-height: 40px; }
  .details { position: absolute; left: 0; width: 768px; display: flex; justify-content: center; align-items: center; gap: 12px; font-size: 22px; }
  .details.when { top: 822px; }
  .details.where { top: 873px; }
  .details.room { top: 914px; }
  .details .gap { width: 8px; }
  .icon-dot { width: 36px; height: 36px; border-radius: 50%; background: var(--orange); display: inline-flex; align-items: center; justify-content: center; flex: none; }
  .footer-rule { position: absolute; left: 32px; top: 972px; width: 706px; height: 1px; background: var(--rule); }
  .footer-brand { position: absolute; left: 70px; top: 1008px; font-weight: 700; font-size: 44px; letter-spacing: 1px; }
  .contact { position: absolute; left: 270px; top: 982px; font-size: 30px; line-height: 38px; font-style: normal; }
  .contact-row { display: flex; align-items: center; gap: 10px; }
  .contact-row svg { flex: none; }
</style>
</head>
<body>
<div class="sheet-frame"></div>
<main class="flyer">
  <div class="hero-photo" role="img" aria-label="Photo: sunset sky with raised cupped hands holding a cross"></div>
  <div class="brand-box"><span class="brand-name">VELODU</span></div>
  <h1 class="event-title"><span class="line-one">Radiant Harvest</span><span class="line-two">Worship Day</span></h1>

  <section class="tagline-band">
    <p class="retreat">A one day prayer retreat.</p>
    <p class="lordship">Jesus Chris is Lord</p>
  </section>

  <section class="keywords">
    <p>Prayer | Sharing the Word</p>
    <p>Panel discussion | Prophecy | Impartation.</p>
  </section>

  <div class="details when">
    <span class="icon-dot"><svg width="20" height="20" viewBox="0 0 20 20" fill="none" stroke="#fff" stroke-width="1.5"><rect x="2" y="4" width="16" height="14"/><line x1="2" y1="8" x2="18" y2="8"/><line x1="6" y1="2" x2="6" y2="5"/><line x1="14" y1="2" x2="14" y2="5"/></svg></span>
    <span>Tuesday July 2nd, 2019</span>
    <span class="gap"></span>
    <span class="icon-dot"><svg width="22" height="22" viewBox="0 0 22 22" fill="none" stroke="#fff" stroke-width="1.6"><circle cx="11" cy="11" r="8"/><polyline points="11,6 11,11 14,13"/></svg></span>
    <span>11:00AM - 7:00PM</span>
  </div>

  <div class="details where">
    <span class="icon-dot"><svg width="20" height="22" viewBox="0 0 20 22" fill="none" stroke="#fff" stroke-width="1.5"><path d="M10 20 C4 13 4 10 4 8 a6 6 0 0 1 12 0 c0 2 0 5-6 12z"/><circle cx="10" cy="8" r="2"/></svg></span>
    <span>Wexmoor Hotel, 4817 Ballard Avenue, Portland, Maine 04102</span>
  </div>
  <div class="details room"><span>(Room: Larkspur)</span></div>

  <div class="footer-rule"></div>
  <div class="footer-brand">VELODU</div>
  <address class="contact">
    <div class="contact-row">
      <svg width="26" height="26" viewBox="0 0 26 26" fill="none" stroke="#fff" stroke-width="1.5"><circle cx="13" cy="13" r="11"/><ellipse cx="13" cy="13" rx="5" ry="11"/><line x1="2" y1="13" x2="24" y2="13"/><line x1="4" y1="7" x2="22" y2="7"/><line x1="4" y1="19" x2="22" y2="19"/></svg>
      <span>velodu.org</span>
      <svg width="30" height="22" viewBox="0 0 30 22" fill="none" stroke="#fff" stroke-width="1.5" style="margin-left:6px"><path d="M3 8 C3 2 27 2 27 8 L22 9 L21 6 C17 5 13 5 9 6 L8 9z"/><rect x="7" y="11" width="16" height="9" rx="2"/></svg>
      <span>207 555 0148</span>
    </div>
    <div class="contact-row">
      <svg width="26" height="20" viewBox="0 0 26 20" fill="none" stroke="#fff" stroke-width="1.5"><rect x="2" y="3" width="22" height="14"/><polyline points="2,3 13,11 24,3"/></svg>
      <span>contact@brightmeadow.org</span>
    </div>
  </address>
</main>
</body>
</html>
```